Chiropractic Flyers to be made more up to date

I have used this series of flyers for my own practice. I would like the graphics to be brought up to date and the name of the doctor and the practice, the address, phone number and date to be removed and a blank box inserted in one place on the flyer that other chiropractors could use to personalize the flyers for their practice. On some of the flyers, this information is in several places. I'd like to have it all in one space so that it would be easy for the doctor to add it in their practice. They all need to be bright and colorful with catchy graphics.

```html
<!DOCTYPE html>
<html lang="en">
<head>
<meta charset="utf-8">
<title>Chiropractic Flyers</title>
<link href="https://fonts.googleapis.com/css2?family=Cinzel:wght@400;600;700&family=Archivo+Black&family=Roboto+Condensed:ital,wght@0,400;0,700;1,400&display=swap" rel="stylesheet">
<style>
  :root{
    --backdrop:#6b6e73;
    --slate-mid:#595c63;
    --slate-bottom:#43464c;
    --teal-deep:#16757b;
    --teal-glow:#1ad3e2;
    --cyan-accent:#2ad4e6;
    --paper:#ffffff;
    --paper-shade:#e4e4e4;
    --ink:#2f2f2f;
    --ink-soft:#4a4a4a;
    --sketch-light:#f2f2f2;
    --sketch-dark:#bdbdbd;
  }
  *{box-sizing:border-box;margin:0;padding:0}
  html,body{width:1200px;height:1000px;overflow:hidden}
  body{background:var(--backdrop);position:relative;font-family:"Roboto Condensed",sans-serif}
  .flyer{position:absolute;top:108px;width:547px;height:774px;overflow:hidden}
  .flyer--reward{left:38px}
  .flyer--fair{left:617px}
  .flyer__body{position:absolute;left:0;top:0;width:100%;height:610px;color:var(--paper);text-align:center}
  .flyer--reward .flyer__body{background:radial-gradient(ellipse 60% 45% at 50% 38%,#6e7178 0%,var(--slate-mid) 55%,var(--slate-bottom) 100%)}
  .flyer--fair .flyer__body{background:radial-gradient(ellipse 55% 45% at 50% 45%,var(--teal-glow) 0%,#18a5b1 40%,var(--teal-deep) 85%)}
  .flyer__title{font-family:"Cinzel",serif;font-weight:600;color:var(--paper);letter-spacing:1px}
  .flyer--reward .flyer__title{position:absolute;top:44px;width:100%;font-size:84px;line-height:1}
  .flyer--fair .flyer__title{position:absolute;top:38px;width:100%;font-size:56px;line-height:52px}
  .notch{position:absolute;top:609px;left:256px;z-index:2}
  .contact-band{position:absolute;left:0;top:610px;width:100%;height:164px;background:linear-gradient(var(--paper) 0%,var(--paper) 45%,var(--paper-shade) 100%);text-align:center;color:var(--ink)}
  .contact-band__name{font-family:"Cinzel",serif;font-weight:600;font-size:45px;margin-top:36px;line-height:1;letter-spacing:1px}
  .contact-band__address{font-family:"Cinzel",serif;font-size:14px;margin-top:-2px;color:var(--ink-soft)}
  .contact-band__lines{font-family:"Cinzel",serif;font-size:12.5px;margin-top:14px;color:var(--ink-soft)}
  .contact-band__lines span{margin:0 8px}

  .wanted-poster{position:absolute;left:127px;top:160px;width:294px;height:302px;background:var(--paper);border:3px solid #000;color:#000}
  .wanted-poster__heading{font-family:"Archivo Black",sans-serif;font-size:56px;line-height:60px;letter-spacing:1px;margin-top:-2px}
  .wanted-poster__sub{font-size:12px;margin-top:4px;letter-spacing:.2px}
  .wanted-poster__sketch{position:absolute;left:52px;top:90px;width:200px;height:205px;background:radial-gradient(ellipse at 60% 45%,var(--sketch-dark) 0%,var(--sketch-light) 75%)}
  .reward-copy{position:absolute;top:496px;left:47px;width:453px;font-size:10.5px;line-height:15px}
  .reward-copy strong{color:var(--cyan-accent);font-weight:700}
  .disclaimer{position:absolute;top:572px;width:100%;font-size:7px;font-style:italic;opacity:.9}

  .people-art{position:absolute;left:133px;top:212px;width:282px;height:210px;border-radius:40px 40px 10px 10px;background:linear-gradient(90deg,#7b85b8 0%,#8b8fb5 45%,#e07a62 55%,#e88069 100%);opacity:.9}
  .highlights{position:absolute;top:478px;left:0;width:100%;height:90px}
  .highlight{position:absolute;top:0;width:112px;transform:translateX(-50%)}
  .highlight h3{font-size:12px;font-weight:700;margin-bottom:6px;white-space:nowrap}
  .highlight p{font-size:10.8px;line-height:12.3px}
</style>
</head>
<body>

<section class="flyer flyer--reward">
  <div class="flyer__body">
    <h1 class="flyer__title">REWARD</h1>
    <div class="wanted-poster">
      <div class="wanted-poster__heading">WANTED</div>
      <div class="wanted-poster__sub">DESPERATE MAN IN NEED OF CHIROPRACTIC CARE</div>
      <div class="wanted-poster__sketch" role="img" aria-label="Pencil sketch of a suspect in a knit cap and sunglasses, with a short suspect description"></div>
    </div>
    <p class="reward-copy">Desperate person in pain. May look like they have a bad headache, stiff neck or low back pain. They may even look like they have a lot of pain between the shoulder blades, at the elbow or knee. If you see this person please be advised they may be grumpy and in need of Chiropractic care. There is a <strong>REWARD OF A FAMILY-SIZED TURKEY</strong> for any desperate character brought in fitting the description <strong>DURING THE HOLIDAY MONTH.</strong></p>
    <p class="disclaimer">*Offer not valid for Medicare, worker's comp. or personal injury cases.</p>
  </div>
  <div class="contact-band">
    <div class="contact-band__name">Doctor's Name</div>
    <div class="contact-band__address">Address, City, State</div>
    <div class="contact-band__lines"><span>Telephone (555) 123-4567</span>|<span>Email Name@Domain.com</span></div>
  </div>
  <svg class="notch" width="34" height="18" viewBox="0 0 34 18" aria-hidden="true"><polygon points="0,0 34,0 17,18" fill="#43464c"/></svg>
</section>

<section class="flyer flyer--fair">
  <div class="flyer__body">
    <h1 class="flyer__title">EMPLOYEE<br>HEALTH FAIR</h1>
    <div class="people-art" role="img" aria-label="Flat illustration of two employees, a man in a suit and tie and a woman in a coral blazer"></div>
    <div class="highlights">
      <div class="highlight" style="left:88px"><h3>Healthy Fun for Everyone!</h3><p>Win prizes, play games, enjoy healthy snacks, and have fun as you find easy ways to bring more health into your life.</p></div>
      <div class="highlight" style="left:227px"><h3>Know Your Numbers!</h3><p>Have your metabolic screenings (including glucose, blood pressure, cholesterol, and waist circumference).</p></div>
      <div class="highlight" style="left:358px"><h3>Win Prizes!</h3><p>Complete an activity at each booth. The more you play, the greater your chances to win a prize of your choice.</p></div>
      <div class="highlight" style="left:480px"><h3>Fitness Demos</h3><p>Fitness demos, including workouts you can do at home, and get fitted for your spin bike.</p></div>
    </div>
    <p class="disclaimer">*Offer not valid for Medicare, worker's comp. or personal injury cases.</p>
  </div>
  <div class="contact-band">
    <div class="contact-band__name">Doctor's Name</div>
    <div class="contact-band__address">Address, City, State</div>
    <div class="contact-band__lines"><span>Telephone (555) 123-4567</span>|<span>Email Name@Domain.com</span></div>
  </div>
  <svg class="notch" width="34" height="18" viewBox="0 0 34 18" aria-hidden="true"><polygon points="0,0 34,0 17,18" fill="#16757b"/></svg>
</section>

</body>
</html>
```